Social Media Marketing company needs a logo (tweak) and business card design

We need to slightly tidy up our logo, mainly to make sure we have the right design file (AI file type) also if possible remove the text below, for the business card we would like to get a fun yet professional feeling since we focus on social media marketing as well as event management
Target Market(s)
All industry really, just trying to look fun and professional to every one.
Industry/Entity Type
Marketing
Contact Information for Business Card
The Business Card needed to be fun yet professional
Font styles to use
Sans Serif
Colors
85cae6
Requirements
Must have
- The Logo.
- On the Name area, please provide two spaces 1. for English and Chinese.
- Rest is English only.
- Do not include a post code space.
- Phone number.
- Also please add website address www.brellavo.com
Nice to have
- Some water marks would be nice.
- Also the slogan "bright moves every day"

```html
<!DOCTYPE html>
<html lang="en">
<head>
<meta charset="utf-8">
<title>Brellavo Business Card</title>
<link rel="stylesheet" href="https://fonts.googleapis.com/css2?family=Montserrat:wght@400;500;600;700&family=Noto+Sans+SC:wght@500&display=swap">
<style>
  :root {
    --backdrop: #2b2b2d;
    --card: #050505;
    --ink: #ffffff;
    --ink-soft: #e6e6e6;
    --watermark: #1c1c1e;
    --accent: #85cae6;
  }
  * { margin: 0; padding: 0; box-sizing: border-box; }
  html, body {
    width: 1200px; height: 900px; overflow: hidden;
    background: var(--backdrop);
    font-family: "Montserrat", sans-serif;
  }
  .canvas { position: relative; width: 1200px; height: 900px; }
  .card {
    position: absolute;
    width: 560px; height: 320px;
    background: var(--card);
    border-radius: 22px;
    box-shadow: 0 14px 30px rgba(0,0,0,0.45);
    overflow: hidden;
    color: var(--ink);
  }
  .card-front { left: 60px; top: 100px; }
  .card-back { left: 580px; top: 480px; }

  /* watermarks */
  .watermark {
    position: absolute;
    color: var(--watermark);
    font-weight: 500;
    white-space: nowrap;
    pointer-events: none;
  }
  .card-front .watermark { left: 50%; top: 34px; transform: translateX(-50%); font-size: 96px; }
  .card-back .watermark { right: -20px; bottom: 10px; font-size: 80px; }

  /* front */
  .brand-mark {
    position: absolute; left: 50%; top: 58px; transform: translateX(-50%);
    width: 70px; height: 70px; border-radius: 50%; background: var(--ink);
  }
  .brand {
    position: absolute; left: 0; right: 0; top: 160px;
    text-align: center;
    font-size: 32px; font-weight: 500; letter-spacing: 0.5px;
  }
  .slogan {
    position: absolute; right: 34px; top: 214px;
    color: var(--accent); font-size: 14px; font-weight: 600;
    letter-spacing: 1.2px; text-transform: uppercase;
  }
  .site-front {
    position: absolute; left: 34px; bottom: 30px;
    font-size: 15px; letter-spacing: 0.4px; color: var(--ink-soft);
  }
  .site-front strong, .contact-web strong { color: var(--accent); font-weight: 700; }

  /* back */
  .brand-small {
    position: absolute; right: 34px; top: 34px;
    display: flex; align-items: center; gap: 8px;
    font-size: 20px; font-weight: 500;
  }
  .brand-small .brand-dot { width: 10px; height: 10px; border-radius: 50%; background: var(--ink); }
  .edge-notch {
    position: absolute; left: -22px; top: 238px;
    width: 44px; height: 44px; border-radius: 50%; background: var(--ink);
  }
  .holder { position: absolute; left: 52px; top: 104px; }
  .holder-name { color: var(--accent); font-size: 24px; font-weight: 600; letter-spacing: 0.4px; line-height: 30px; }
  .holder-name-cn {
    font-family: "Noto Sans SC", sans-serif;
    color: var(--accent); font-size: 17px; font-weight: 500; line-height: 24px; letter-spacing: 2px;
  }
  .holder-role { font-size: 14px; color: var(--ink-soft); line-height: 20px; }
  .contact { list-style: none; margin-top: 6px; font-size: 15px; line-height: 21px; color: var(--ink-soft); }
  .contact li { display: flex; align-items: center; gap: 8px; }
  .contact .icon { width: 11px; height: 11px; flex: none; }
  .contact .indent { padding-left: 19px; }
</style>
</head>
<body>
<main class="canvas">
  <section class="card card-front">
    <span class="watermark" aria-hidden="true">Brellavo</span>
    <span class="brand-mark"></span>
    <div class="brand">Brellavo</div>
    <p class="slogan">Bright moves every day</p>
    <p class="site-front">www.<strong>brellavo</strong>.com</p>
  </section>

  <section class="card card-back">
    <span class="watermark" aria-hidden="true">Brellavo</span>
    <div class="brand-small"><span class="brand-dot"></span>Brellavo</div>
    <span class="edge-notch"></span>
    <div class="holder">
      <h1 class="holder-name">Marlon Keats</h1>
      <p class="holder-name-cn" lang="zh">马龙·基茨</p>
      <p class="holder-role">Director</p>
      <ul class="contact">
        <li class="indent">48 Harbor Lane</li>
        <li class="indent">Eastfield, NY</li>
        <li>
          <svg class="icon" viewBox="0 0 12 12"><path fill="#85cae6" d="M2.5 1 L4.5 1 L5.2 3.6 L4 4.6 Q5 7 7.4 8 L8.4 6.8 L11 7.5 L11 9.5 Q10.5 11 9 11 Q1 10 1 2.5 Q1 1 2.5 1Z"/></svg>
          +330 5812-3904
        </li>
        <li>
          <svg class="icon" viewBox="0 0 12 12"><rect x="0.8" y="2.2" width="10.4" height="7.6" fill="none" stroke="#85cae6" stroke-width="1.3"/><path d="M1 2.6 L6 6.6 L11 2.6" fill="none" stroke="#85cae6" stroke-width="1.3"/></svg>
          info@brellavo.com
        </li>
        <li class="contact-web">
          <svg class="icon" viewBox="0 0 12 12"><circle cx="6" cy="6" r="5" fill="none" stroke="#85cae6" stroke-width="1.3"/><path d="M1 6 H11 M6 1 Q3 6 6 11 Q9 6 6 1" fill="none" stroke="#85cae6" stroke-width="1"/></svg>
          <span>www.<strong>brellavo</strong>.com</span>
        </li>
      </ul>
    </div>
  </section>
</main>
</body>
</html>
```